Chai Tea Company needs a Tea Packaging Box Design

Tea Packaging
Dimensions of the Tea Packaging Box: Height 13 cm; Width 8.5 cm; Depth 7 cm
Individual Teabag Packet/ Sachet: Width 6.5 cm; Length 8.25 cm
We are looking for a new tea packaging design, for our tea business. The material of the box is cardboard. We are also looking for a design that will be on each individual tea bag sachet/packet that goes into the box. This design will be very similar to what you design for the tea packaging box.
Product Info:
Our tea company is called “Marlow Loft”. We sell two types of Chai Tea, once called “Ember Blend” and one called “Meadow Tisane”. The Ember Blend has caffeine, while the Meadow Tisane is Naturally Caffeine Free. The Ember Blend has a black tea base, while the Meadow Tisane has a Rooibos tea base. We will need two tea packaging designs, one for each Chai Tea flavour. The designs for both the teas can be similar, but make sure that you can easily distinguish one from the other (example: make them have different colours or pictures). Both the chai teas, come from the same product line.
Tea Packaging Design:
We are looking for high end tea packaging. We produce high quality teas, and we would like to portray this in our tea packaging. Our teas are made with no artificial flavourings, natural flavourings, or preservatives, so we would also like a natural, organic, high quality look to our tea packaging. Our current logo is a llama. It would be great if you could make the current logo more polished and well made. If you feel that the llama is not well suited or you would like to design the llama differently, we are open to your creative ideas.
General Basic Info:
Keep in mind, we will have both English and French writing on the tea packaging. You do not need to worry about the French writing (we will do the translation), just make sure there is room for it. However, if you feel that you are capable and knowledgeable of incorporating both French and English language into the tea packaging that would be of great help and value.
Back of the Box:
- Will have ingredients and brewing instructions. Basic brewing instructions are: “Add hot water to teabag. Steep for 5-7 minutes, depending on strength preferred. Add milk and your choice of sweetener. Enjoy! See inside panel of box for more detailed instructions”. (The basic brewing instructions, can further be polished or written in a more creative or professional manner).
Front of the Box:
- Will have company name, type of tea, little description of the tea
- 18 teabags
- 54 g (1.9 OZ)
- Should state that this is a product of Alberta, Canada.
Side of the Box:
Any creative wording, slogan, or description about the tea, or whatever you feel would be good on the side of the box.
On the inside flap of the side of the box, there will be detailed instructions on how to brew the tea. These will be different from the simplified brewing instructions on the back of the box. I have attached the advanced brewing instructions as a file. These instructions can further be simplified or reduced to make it easier and cleaner for the consumers to read.
Individual Tea Sachets/ Packets
- These will have a matching look and design of the tea box packaging, except on a smaller scale. Each individual sachet will have the company name, type of tea, little description of the tea in the front of the sachet, while the back will contain the ingredients, and basic brewing instructions.
I have attached a few files, with the dimensions, ingredients, detailed brewing directions, and current logo of the business.
If you have any questions, about the design or packaging please let me know. The winning designer will be required to do a few additional tweaks to finalize the product. Thank you for your time and happy designing!

```html
<!DOCTYPE html>
<html lang="en">
<head>
<meta charset="utf-8">
<title>Marlow Loft – Ember Blend Chai Tea Packaging</title>
<link rel="stylesheet" href="https://fonts.googleapis.com/css2?family=Alegreya+Sans+SC:wght@500;700&family=Courgette&family=Roboto+Condensed:wght@400;700&display=swap">
<style>
  :root {
    --backdrop: #eeeeee;
    --kraft-light: #ece5cf;
    --kraft: #e0d6b8;
    --kraft-dark: #d2c6a2;
    --green: #3fa65a;
    --green-deep: #2f8f4a;
    --green-soft: #bcd9a8;
    --ink: #2a2a26;
    --ink-soft: #4a463c;
    --tea-red: #8e1c1c;
    --white: #ffffff;
    --head-font: "Alegreya Sans SC", "Trebuchet MS", sans-serif;
    --script-font: "Courgette", cursive;
    --body-font: "Roboto Condensed", "Arial Narrow", sans-serif;
  }
  * { box-sizing: border-box; margin: 0; padding: 0; }
  html, body { width: 1200px; height: 1200px; overflow: hidden; background: var(--backdrop); }
  .canvas { position: relative; width: 1200px; height: 1200px; font-family: var(--body-font); color: var(--ink); }

  .panel {
    position: absolute;
    background: linear-gradient(160deg, var(--kraft-light) 0%, var(--kraft) 60%, var(--kraft-dark) 100%);
    box-shadow: 0 2px 10px rgba(0,0,0,0.12);
    overflow: hidden;
  }
  .panel-side  { left: 90px;  top: 60px; width: 280px; height: 560px; }
  .panel-front { left: 400px; top: 60px; width: 340px; height: 560px; }
  .panel-back  { left: 770px; top: 60px; width: 340px; height: 560px; }
  .panel-flap  { left: 400px; top: 660px; width: 710px; height: 330px; }
  .sachet      { left: 90px;  top: 660px; width: 280px; height: 360px; }

  /* brand lockup */
  .brand { display: flex; align-items: center; justify-content: center; gap: 8px; }
  .brand-dot { width: 14px; height: 14px; border-radius: 50%; background: var(--green); }
  .brand-name { font-family: var(--head-font); font-weight: 500; color: var(--ink); letter-spacing: 0.5px; }

  .title { font-family: var(--head-font); font-weight: 700; color: var(--green); line-height: 0.95; }
  .variant { font-family: var(--head-font); font-weight: 700; color: var(--green); }

  .script { font-family: var(--script-font); color: var(--ink-soft); line-height: 1.3; }

  .caffeine-badge {
    position: absolute;
    background: var(--green);
    color: var(--white);
    font-family: var(--head-font);
    font-weight: 700;
    text-align: center;
    line-height: 1.05;
    border-radius: 6px;
    border: 2px solid var(--white);
    box-shadow: 0 0 0 1px var(--green);
  }

  .art { position: absolute; display: block; }

  .band {
    position: absolute; left: 0; right: 0;
    background: var(--green);
    color: var(--white);
    font-family: var(--head-font);
    font-weight: 700;
    text-align: right;
  }

  .meta { position: absolute; font-size: 10px; font-weight: 700; color: var(--ink); }

  /* side panel */
  .side-copy { position: absolute; top: 40px; left: 22px; right: 22px; font-size: 14px; }
  .side-copy p + p { margin-top: 14px; }

  /* front panel */
  .front-brand { position: absolute; top: 40px; left: 0; right: 0; }
  .front-brand .brand-name { font-size: 22px; }
  .front-title { position: absolute; top: 110px; left: 26px; right: 20px; }
  .front-title .title { font-size: 38px; }
  .front-title .variant { font-size: 19px; margin-top: 8px; }
  .front-desc { position: absolute; top: 215px; left: 26px; right: 26px; font-size: 11.5px; }
  .front-desc p + p { margin-top: 8px; }

  /* back panel */
  .back-body { position: absolute; top: 34px; left: 26px; right: 22px; }
  .back-body .title { font-size: 30px; }
  .back-body .variant { font-size: 16px; margin-top: 6px; }
  .steps { list-style: none; margin-top: 14px; font-size: 10.5px; line-height: 1.45; }
  .steps li::before { content: "• "; font-weight: 700; }
  .ingredients-head { font-family: var(--head-font); font-weight: 700; font-size: 14px; margin-top: 10px; }
  .ingredients { display: grid; grid-template-columns: 1fr 1fr; font-size: 10px; line-height: 1.4; list-style: none; margin-top: 2px; }
  .ingredients li::before { content: "• "; }
  .ingredients .wide { grid-column: 1 / 3; }
  .rule { height: 3px; background: var(--green); margin: 12px 0; }

  /* inside flap */
  .flap-cols { position: absolute; inset: 26px 30px; display: grid; grid-template-columns: 1fr 1fr; gap: 36px; }
  .flap-steps { font-size: 12.5px; line-height: 1.5; padding-left: 18px; }
  .flap-steps li + li { margin-top: 6px; }
  .flap-divider { position: absolute; top: 26px; bottom: 26px; left: 355px; width: 1px; background: var(--green); }

  /* sachet */
  .sachet-brand { position: absolute; top: 26px; left: 0; right: 0; }
  .sachet-brand .brand-name { font-size: 16px; }
  .sachet-brand .brand-dot { width: 10px; height: 10px; }
  .sachet-title { position: absolute; top: 64px; left: 20px; right: 16px; }
  .sachet-title .title { font-size: 26px; }
  .sachet-title .variant { font-size: 14px; margin-top: 4px; }
  .sachet-desc { position: absolute; top: 132px; left: 20px; width: 150px; font-size: 9.5px; }
  .sachet-desc p + p { margin-top: 4px; }
</style>
</head>
<body>
<main class="canvas">

  <!-- side panel -->
  <section class="panel panel-side" aria-label="Box side panel">
    <div class="side-copy script">
      <p>An exotic blend of black tea, cardamom, fennel, cloves, Cinnamon, and ginger.</p>
      <p>Un mélange exotique de thé noir, de cardamome, fenouil, clous de girofle, la cannelle et le gingembre.</p>
    </div>
    <div class="caffeine-badge" style="left:22px; top:260px; width:76px; padding:5px 0; font-size:12px;">CAFFEINE<br>CAFÉINE</div>
    <svg class="art" style="left:110px; top:236px;" width="140" height="110" viewBox="0 0 140 110" role="img" aria-label="Glass cup of red chai tea with loose tea leaves">
      <defs>
        <radialGradient id="cupSide" cx="50%" cy="45%" r="60%">
          <stop offset="0" stop-color="#a8262a"/>
          <stop offset="0.7" stop-color="#7d1a1a"/>
          <stop offset="1" stop-color="#c8c3ae" stop-opacity="0"/>
        </radialGradient>
      </defs>
      <rect width="140" height="110" fill="url(#cupSide)"/>
    </svg>
  </section>

  <!-- front panel -->
  <section class="panel panel-front" aria-label="Box front panel">
    <svg class="art" style="left:0; top:250px;" width="340" height="180" viewBox="0 0 340 180" role="img" aria-label="Faint green sketch of rolling tea fields and trees">
      <defs>
        <linearGradient id="fieldFront" x1="0" y1="0" x2="0" y2="1">
          <stop offset="0" stop-color="#bcd9a8" stop-opacity="0"/>
          <stop offset="1" stop-color="#bcd9a8" stop-opacity="0.55"/>
        </linearGradient>
      </defs>
      <rect width="340" height="180" fill="url(#fieldFront)"/>
    </svg>

    <div class="front-brand brand">
      <span class="brand-dot"></span>
      <span class="brand-name">MARLOW LOFT</span>
    </div>
    <div class="front-title">
      <h1 class="title">Chai Tea<br>Thé Chai</h1>
      <p class="variant">Ember Blend - Mélange Braise</p>
    </div>
    <div class="front-desc script">
      <p>An exotic blend of black tea, cardamom, fennel, cloves, Cinnamon, and ginger.</p>
      <p>Un mélange exotique de thé noir, de cardamome, fenouil, clous de girofle, la cannelle et le gingembre.</p>
    </div>

    <div class="caffeine-badge" style="left:24px; top:348px; width:76px; padding:5px 0; font-size:12px;">CAFFEINE<br>CAFÉINE</div>
    <svg class="art" style="left:110px; top:320px;" width="200" height="150" viewBox="0 0 200 150" role="img" aria-label="Glass cup of red chai tea with loose tea leaves">
      <defs>
        <radialGradient id="cupFront" cx="50%" cy="45%" r="60%">
          <stop offset="0" stop-color="#a8262a"/>
          <stop offset="0.65" stop-color="#7d1a1a"/>
          <stop offset="1" stop-color="#c8c3ae" stop-opacity="0"/>
        </radialGradient>
      </defs>
      <rect width="200" height="150" fill="url(#cupFront)"/>
    </svg>

    <div class="band" style="top:478px; height:40px; padding:4px 14px 0 0; font-size:15px; line-height:1.05;">
      Chai Tea &nbsp;Thé Chai<br><span style="font-size:12px;">Ember Blend - Mélange Braise</span>
    </div>
    <p class="meta" style="left:20px; top:528px;">18 teabags | 54 g (1.9 OZ)</p>
    <p class="meta" style="right:20px; top:526px; line-height:1.2;">Product of | produit de<br>ALBERTA, CANADA</p>
  </section>

  <!-- back panel -->
  <section class="panel panel-back" aria-label="Box back panel">
    <div class="back-body">
      <h2 class="title">Chai Tea<br>Thé Chai</h2>
      <p class="variant">Ember Blend - Mélange Braise</p>
      <ul class="steps">
        <li>Add hot water to teabag.</li>
        <li>Steep for 5-7 minutes, depending on strength preferred.</li>
        <li>Add milk and your choice of sweetener.</li>
        <li>Enjoy! See inside panel of box for more detailed instructions</li>
      </ul>
      <p class="ingredients-head">INGREDIENTS:</p>
      <ul class="ingredients">
        <li>1½ cups (12 oz) water.</li>
        <li>2 Chai tea bags.</li>
        <li>1cup (8oz) (whole) milk.</li>
        <li>2-4 teaspoons sugar or honey to taste</li>
        <li class="wide">2 teaspoons of sliced or grated fresh ginger (optional)</li>
      </ul>
      <div class="rule"></div>
      <ul class="steps" style="margin-top:0;">
        <li>Add hot water to teabag.</li>
        <li>Steep for 5-7 minutes, depending on strength preferred.</li>
        <li>Add milk and your choice of sweetener.</li>
        <li>Enjoy! See inside panel of box for more detailed instructions</li>
      </ul>
      <p class="ingredients-head">INGREDIENTS:</p>
      <ul class="ingredients">
        <li>1½ cups (12 oz) water.</li>
        <li>2 Chai tea bags.</li>
        <li>1cup (8oz) (whole) milk.</li>
        <li>2-4 teaspoons sugar or honey to taste</li>
        <li class="wide">2 teaspoons of sliced or grated fresh ginger (optional)</li>
      </ul>
    </div>
    <p class="meta" style="left:26px; top:528px;">18 teabags | 54 g (1.9 OZ)</p>
    <p class="meta" style="right:20px; top:522px; line-height:1.2;">Product of | produit de<br>ALBERTA, CANADA</p>
  </section>

  <!-- inside flap: detailed brewing -->
  <section class="panel panel-flap" aria-label="Inside flap with detailed brewing instructions">
    <div class="flap-divider"></div>
    <div class="flap-cols">
      <ol class="flap-steps">
        <li>Bring water and tea bags to a low boil in a covered pot.</li>
        <li>Turn down heat, keep covered, and simmer for 6 minutes. Stir and gently press or squeeze bags, two or three times while simmering, to help release flavour.</li>
        <li>Add ginger and milk. From time to time open cover and stir until Chai starts simmering again.</li>
        <li>Turn off heat, add sugar, stir, and allow to steep covered for a further 3 to 5 minutes. Strain into cups and enjoy.</li>
      </ol>
      <ol class="flap-steps">
        <li>Bring water and tea bags to a low boil in a covered pot.</li>
        <li>Turn down heat, keep covered, and simmer for 6 minutes. Stir and gently press or squeeze bags, two or three times while simmering, to help release flavour.</li>
        <li>Add ginger and milk. From time to time open cover and stir until Chai starts simmering again.</li>
        <li>Turn off heat, add sugar, stir, and allow to steep covered for a further 3 to 5 minutes. Strain into cups and enjoy.</li>
      </ol>
    </div>
  </section>

  <!-- sachet front -->
  <section class="panel sachet" aria-label="Teabag sachet front">
    <svg class="art" style="left:0; top:150px;" width="280" height="140" viewBox="0 0 280 140" role="img" aria-label="Faint green sketch of rolling tea fields and trees">
      <defs>
        <linearGradient id="fieldSachet" x1="0" y1="0" x2="0" y2="1">
          <stop offset="0" stop-color="#bcd9a8" stop-opacity="0"/>
          <stop offset="1" stop-color="#bcd9a8" stop-opacity="0.55"/>
        </linearGradient>
      </defs>
      <rect width="280" height="140" fill="url(#fieldSachet)"/>
    </svg>
    <div class="sachet-brand brand">
      <span class="brand-dot"></span>
      <span class="brand-name">MARLOW LOFT</span>
    </div>
    <div class="sachet-title">
      <h3 class="title">Chai Tea<br>Thé Chai</h3>
      <p class="variant">Ember Blend - Mélange Braise</p>
    </div>
    <div class="sachet-desc script">
      <p>An exotic blend of black tea, cardamom, fennel, cloves, Cinnamon, and ginger.</p>
      <p>Un mélange exotique de thé noir, de cardamome, fenouil, clous de girofle, la cannelle et le gingembre.</p>
    </div>
    <svg class="art" style="left:120px; top:220px;" width="150" height="100" viewBox="0 0 150 100" role="img" aria-label="Glass cup of red chai tea with loose tea leaves">
      <defs>
        <radialGradient id="cupSachet" cx="50%" cy="45%" r="60%">
          <stop offset="0" stop-color="#a8262a"/>
          <stop offset="0.65" stop-color="#7d1a1a"/>
          <stop offset="1" stop-color="#c8c3ae" stop-opacity="0"/>
        </radialGradient>
      </defs>
      <rect width="150" height="100" fill="url(#cupSachet)"/>
    </svg>
    <div class="caffeine-badge" style="left:20px; top:262px; width:60px; padding:4px 0; font-size:10px;">CAFFEINE<br>CAFÉINE</div>
    <div class="band" style="top:316px; height:10px;"></div>
    <p class="meta" style="left:20px; top:300px; font-size:9px;">Weight: 3 g</p>
    <p class="meta" style="left:20px; top:334px; font-size:9px;">Product of | produit de: ALBERTA, CANADA</p>
  </section>

</main>
</body>
</html>
```